Dale Winslow Drum Demo

My husband and I just moved to Nashville. Dale (my husband) is a drummer with 30 years of experience. We have a CD that we would like to promote with hope that he can get a gig doing what he loves. We would like your talented artists to create a CD cover and label. We are here to promote Dale, although we also think the rest of the band should be mentioned and recognized. I am going to put the names of the musicians as well as two pictures that can be used for the outside cover if necessary. On the inside of the cover I would like the band members mentioned as well as a little bio. about Dale.
Dale Winslow - drums and vocals
Mark Delvey - vocals
Rick Hanlon - bass
Pete Morant - lead guitar

Dale's bio
Born in Massachusetts
30 years experience
some drumming school
local band experience
music played: blues, classic rock, country, jazz, and alternative
influences: Carl Mesner, Lenny Vask, Glen Fosk, Walt Dusek
Great passion, feel, and desire for music....something which cannot be taught!!!

```html
<!DOCTYPE html>
<html lang="en">
<head>
<meta charset="utf-8">
<title>Dale Winslow – CD Package</title>
<link rel="stylesheet" href="https://fonts.googleapis.com/css2?family=Sacramento&family=Quicksand:wght@400;500&display=swap">
<style>
  :root {
    --backdrop: #e4e4e6;
    --red-light: #a81d26;
    --red-mid: #8c161e;
    --red-dark: #5f0c11;
    --ink: #ffffff;
    --ink-soft: rgba(255,255,255,0.88);
    --disc-rim: #d9d9dc;
    --script: "Sacramento", cursive;
    --body: "Quicksand", sans-serif;
  }
  * { box-sizing: border-box; margin: 0; padding: 0; }
  html, body { width: 1200px; height: 800px; overflow: hidden; }
  body {
    background: var(--backdrop);
    font-family: var(--body);
    color: var(--ink);
    display: flex;
    align-items: center;
    justify-content: center;
  }
  .package {
    display: grid;
    grid-template-columns: 360px 360px;
    grid-template-rows: 360px 360px;
    gap: 28px 28px;
  }
  .panel {
    position: relative;
    width: 360px;
    height: 360px;
    background: radial-gradient(circle at 50% 40%, var(--red-light) 0%, var(--red-mid) 50%, var(--red-dark) 100%);
    box-shadow: 0 6px 14px rgba(0,0,0,0.18);
    overflow: hidden;
  }

  /* Front cover */
  .front-cover .artist-name {
    position: absolute;
    top: 62px;
    left: 40px;
    font-family: var(--script);
    font-weight: 400;
    font-size: 50px;
    line-height: 1;
    transform: rotate(-8deg);
    transform-origin: left center;
    white-space: nowrap;
  }
  .front-cover .hand-art {
    position: absolute;
    left: 60px;
    top: 150px;
    width: 240px;
    height: 190px;
  }

  /* Booklet inside */
  .booklet-inside { padding: 30px 30px; font-size: 11.5px; line-height: 1.45; color: var(--ink-soft); }
  .booklet-inside .bio p { margin-bottom: 12px; }
  .booklet-inside .bio .lead-name { text-transform: uppercase; }
  .band-list {
    display: grid;
    grid-template-columns: 1fr 1fr;
    column-gap: 18px;
    margin-top: 10px;
    padding-left: 40px;
  }
  .band-list dt, .band-list dd { margin: 0; }

  /* Disc tray */
  .disc-tray { display: flex; align-items: center; justify-content: center; }
  .disc {
    position: relative;
    width: 320px;
    height: 320px;
    border-radius: 50%;
    background: radial-gradient(circle at 50% 45%, var(--red-light) 0%, var(--red-mid) 60%, var(--red-dark) 100%);
    border: 4px solid var(--disc-rim);
    box-shadow: 0 3px 10px rgba(0,0,0,0.35);
    overflow: hidden;
  }
  .disc .hub {
    position: absolute;
    left: 50%; top: 50%;
    width: 46px; height: 46px;
    margin: -23px 0 0 -23px;
    border-radius: 50%;
    background: radial-gradient(circle, #c23a40 0%, #8e1a20 70%);
    border: 1px solid rgba(255,255,255,0.18);
  }
  .disc .artist-name {
    position: absolute;
    top: 84px;
    left: 32px;
    font-family: var(--script);
    font-weight: 400;
    font-size: 40px;
    line-height: 1;
    transform: rotate(-9deg);
    transform-origin: left center;
    white-space: nowrap;
  }
  .disc .album-title {
    position: absolute;
    top: 196px;
    left: 178px;
    font-size: 12.5px;
    letter-spacing: 0.03em;
    text-transform: uppercase;
    white-space: nowrap;
  }
</style>
</head>
<body>
  <main class="package">
    <section class="panel front-cover">
      <h1 class="artist-name">Dale Winslow</h1>
      <svg class="hand-art" viewBox="0 0 240 190" role="img" aria-label="White silhouette of a hand making the rock sign while holding crossed drumsticks">
        <rect width="240" height="190" fill="#f4f4f4" opacity="0.92"/>
      </svg>
    </section>

    <section class="panel disc-tray">
      <div class="disc">
        <h2 class="artist-name">Dale Winslow</h2>
        <span class="hub"></span>
        <p class="album-title">Album Name</p>
      </div>
    </section>

    <section class="panel booklet-inside">
      <div class="bio">
        <p><span class="lead-name">Dale Winslow</span> was born in Massachusetts. He visited several drumming schools and gained experience in a local band. To this day Dale has got 30 years experience in drumming, he played blues, classic rock, country, jazz and even alternative music.</p>
        <p>Dale's music is influenced by some of the greatest drummers of all time: Carl Mesner, Lenny Vask, Glen Fosk and Walt Dusek.</p>
        <p>Dale has a great passion, feel and desire for music, something which cannot be taught.</p>
        <p>We hope that you enjoy this Album, but all that could not be done without the right people.</p>
      </div>
      <dl class="band-list">
        <dt>Dale Winslow</dt><dd>Drums and vocals</dd>
        <dt>Mark Delvey</dt><dd>Vocals</dd>
        <dt>Rick Hanlon</dt><dd>Bass</dd>
        <dt>Pete Morant</dt><dd>Lead Guitar</dd>
      </dl>
    </section>

    <section class="panel back-cover" aria-label="Back cover"></section>
  </main>
</body>
</html>
```